On-line Christmas Card design

We are a start-up management consulting business in New Zealand and are looking for a design for an on-line Christmas card.
We want to send the "card" out by embedded into an email. We need the whole design to be seen when the email is opened so landscape is probably better.

Target Market(s)

Our clients are senior executives in public and private sector organizations.

Industry/Entity Type

Management Consulting

Requirements
Must have
• Our logo somewhere in the design. Some source files are attached which show our stationery etc. Please don't change the colors of our logo in your design.
Use of our colors - green and gray.
A generic greeting - something referring to happy holidays, seasons greetings, etc rather than "Merry Christmas".

It's summer in NZ so no winter, snow scenes. If you are proposing a photo, then beach scenes are better. We would be interested in designs that are not photos.
Should not have
• Not religious.

```html
<!DOCTYPE html>
<html lang="en">
<head>
<meta charset="utf-8">
<title>Happy Holidays – Kea Consulting</title>
<link rel="stylesheet" href="https://fonts.googleapis.com/css2?family=Great+Vibes&family=Mulish:wght@400&display=swap">
<style>
  :root {
    --sky-top: #2aa6e6;
    --sky-low: #8fd3f2;
    --sea-deep: #1f8fd0;
    --sea-mid: #1fb8d8;
    --sea-light: #6fe0e8;
    --surf: #e8f6f6;
    --sand-light: #f3ece0;
    --sand: #e7dccb;
    --tree-green: #3f6b2e;
    --tree-red: #c8322a;
    --white: #ffffff;
    --glow: rgba(255, 255, 255, 0.75);
    --brand-green: #6bbd2e;
    --brand-gray: #6d6e71;
  }

  html, body {
    margin: 0;
    padding: 0;
    width: 1200px;
    height: 900px;
    overflow: hidden;
    background: var(--white);
  }

  .holiday-card {
    position: relative;
    width: 1200px;
    height: 900px;
    overflow: hidden;
  }

  .beach-scene {
    position: absolute;
    inset: 0;
    background: linear-gradient(
      to bottom,
      var(--sky-top) 0%,
      var(--sky-low) 24%,
      var(--sea-deep) 25.5%,
      var(--sea-mid) 40%,
      var(--sea-light) 60%,
      var(--surf) 66%,
      var(--sand-light) 70%,
      var(--sand) 100%
    );
  }

  .tree-area {
    position: absolute;
    left: 735px;
    top: 370px;
    width: 390px;
    height: 500px;
    border-radius: 45% 45% 20% 20% / 70% 70% 15% 15%;
    background: radial-gradient(ellipse at 50% 55%, var(--tree-green) 0%, rgba(63,107,46,0.7) 45%, rgba(200,50,42,0.35) 75%, rgba(200,50,42,0) 100%);
  }

  .greeting {
    position: absolute;
    left: 0;
    right: 0;
    top: 170px;
    margin: 0;
    text-align: center;
    font-family: "Great Vibes", cursive;
    font-weight: 400;
    font-size: 178px;
    line-height: 1;
    color: var(--white);
    letter-spacing: 2px;
    text-shadow: 0 0 14px var(--glow), 0 0 30px var(--glow);
  }

  .brand-plate {
    position: absolute;
    left: 0;
    top: 683px;
    width: 670px;
    height: 127px;
    background: var(--white);
    display: flex;
    align-items: center;
    gap: 22px;
    padding-left: 38px;
    box-sizing: border-box;
  }

  .brand-mark {
    width: 44px;
    height: 44px;
    background: var(--brand-green);
    flex: none;
  }

  .brand-name {
    font-family: "Mulish", sans-serif;
    font-weight: 400;
    font-size: 64px;
    line-height: 1;
    color: var(--brand-gray);
    white-space: nowrap;
  }
</style>
</head>
<body>
  <main class="holiday-card">
    <div class="beach-scene" role="img" aria-label="Photograph of a sunny tropical beach: blue sky with soft clouds, turquoise sea and white sand"></div>
    <div class="tree-area" role="img" aria-label="Decorated Christmas tree with a star on top and wrapped presents at its base, standing on the sand"></div>

    <h1 class="greeting">Happy Holidays</h1>

    <div class="brand-plate">
      <span class="brand-mark"></span>
      <span class="brand-name">Kea Consulting</span>
    </div>
  </main>
</body>
</html>
```